Design a flyer for food

Propose a design with the given food picture but remove sentence in green on the food picture. The plate needs to be visible. Lighten the picture a little bit to make it attractive.

Keep the design light, luxurious, classy and prestigious.
Colors to use are : Red white or black white (will attach the graphical charter)
Font to use is: Adobe Caslon Pro 12
(will attach the graphical charter)

I have attached the company logo (use only one logo type. The one that fits your design the most.
Keep the Logo large and visible enough on the middle top.

Written content to use is as below:

Tous les Vendredis 

Tchiep poisson ou poulet 

5.000 Fcfa à emporter 
6.000 Fcfa sur place 

?065 318 926 / 065 739 152 / 065
874 263
evenements at korvalisette.com (this is the email address so use the at sign)

```html
<!DOCTYPE html>
<html lang="fr">
<head>
<meta charset="utf-8">
<title>Korvalis – Tous les Vendredis</title>
<link rel="stylesheet" href="https://fonts.googleapis.com/css2?family=Libre+Caslon+Text:wght@400;700&display=swap">
<style>
  :root {
    --ink: #0b0b0b;
    --night: #151515;
    --sheen: #3a3a3a;
    --red: #c0161b;
    --white: #ffffff;
    --text-dark: #111111;
  }
  * { margin: 0; padding: 0; box-sizing: border-box; }
  html, body { width: 872px; height: 1200px; overflow: hidden; background: var(--ink); }
  .flyer {
    position: relative;
    width: 872px;
    height: 1200px;
    overflow: hidden;
    font-family: "Libre Caslon Text", Georgia, serif;
    color: var(--white);
    background:
      linear-gradient(115deg, var(--ink) 0%, var(--night) 30%, var(--sheen) 46%, var(--night) 58%, var(--ink) 75%, #262626 100%);
  }
  .art {
    position: absolute;
    left: 0;
    top: 0;
    width: 872px;
    height: 1200px;
  }
  .brand {
    position: absolute;
    left: 15px;
    top: 160px;
    width: 337px;
    text-align: center;
    font-size: 44px;
    font-weight: 400;
    letter-spacing: 2px;
    line-height: 1;
    color: var(--red);
  }
  .brand-rule {
    position: absolute;
    left: 15px;
    top: 248px;
    width: 337px;
    height: 2px;
    background: var(--red);
  }
  .offer-title {
    position: absolute;
    left: 36px;
    top: 825px;
    font-size: 46px;
    font-weight: 700;
    line-height: 1;
    white-space: nowrap;
  }
  .offer-rule {
    position: absolute;
    left: 29px;
    top: 887px;
    width: 511px;
    height: 3px;
    background: var(--red);
  }
  .offer-line {
    position: absolute;
    left: 36px;
    font-size: 37px;
    font-weight: 400;
    line-height: 1;
    white-space: nowrap;
  }
  .line-dish { top: 918px; }
  .line-takeaway { top: 981px; }
  .line-onsite { top: 1039px; }
  .contact {
    position: absolute;
    left: 330px;
    top: 1124px;
    width: 542px;
    height: 76px;
    background: var(--white);
    border-top-left-radius: 26px;
    color: var(--text-dark);
    padding: 4px 0 0 24px;
    font-size: 24px;
    line-height: 34px;
    white-space: nowrap;
  }
</style>
</head>
<body>
<main class="flyer">
  <svg class="art" viewBox="0 0 872 1200" xmlns="http://www.w3.org/2000/svg">
    <defs>
      <radialGradient id="redMist" cx="0.5" cy="0.5" r="0.5">
        <stop offset="0" stop-color="#c0161b" stop-opacity="0.55"/>
        <stop offset="0.6" stop-color="#9e1014" stop-opacity="0.25"/>
        <stop offset="1" stop-color="#9e1014" stop-opacity="0"/>
      </radialGradient>
      <linearGradient id="dishTones" x1="0" y1="0" x2="1" y2="1">
        <stop offset="0" stop-color="#c99a62"/>
        <stop offset="0.4" stop-color="#9c6a3e"/>
        <stop offset="0.7" stop-color="#5b5a2c"/>
        <stop offset="1" stop-color="#2b2f33"/>
      </linearGradient>
      <clipPath id="canvasClip"><rect width="872" height="1200"/></clipPath>
    </defs>

    <g role="img" aria-label="Texture décorative d'éclaboussures rouges" clip-path="url(#canvasClip)">
      <ellipse cx="540" cy="55" rx="200" ry="75" fill="url(#redMist)"/>
      <ellipse cx="60" cy="520" rx="90" ry="260" fill="url(#redMist)"/>
      <ellipse cx="250" cy="640" rx="80" ry="130" fill="url(#redMist)" opacity="0.7"/>
      <ellipse cx="120" cy="1120" rx="180" ry="110" fill="url(#redMist)"/>
      <ellipse cx="845" cy="300" rx="60" ry="200" fill="url(#redMist)"/>
      <ellipse cx="840" cy="880" rx="70" ry="230" fill="url(#redMist)"/>
    </g>

    <g transform="rotate(24 558 494)">
      <rect x="358" y="194" width="400" height="600" rx="50" fill="url(#dishTones)"
            role="img" aria-label="Photo d'un plat de tchiep au poisson avec légumes et sauce verte"/>
    </g>
    <g transform="rotate(24 538 509)">
      <rect x="349" y="216.5" width="378" height="585" rx="50" fill="none" stroke="var(--white)" stroke-width="7"/>
    </g>
  </svg>

  <div class="brand">KORVALIS</div>
  <div class="brand-rule"></div>

  <h1 class="offer-title">Tous les Vendredis</h1>
  <div class="offer-rule"></div>
  <p class="offer-line line-dish">Tchiep poisson ou poulet</p>
  <p class="offer-line line-takeaway">5.000 Fcfa à emporter</p>
  <p class="offer-line line-onsite">6.000 Fcfa sur place</p>

  <footer class="contact">
    <p>065 318 926 / 065 739 152 / 065 874 263</p>
    <p>evenements@korvalisette.com</p>
  </footer>
</main>
</body>
</html>
```